Designs for a fundrasining event a Brown Tie Beer and Wine event

We need a flyer, brochure, and tickets for entry for a brown tie event that will be a beer and wine pairing fundraising event to be held on May 9th from 6pm to 10pm at the harborview Bistro in Cedar Lake, Indiana, USA. There will be approximately 10 silent auction items and 5 or so sponsors that we will want to have the logos of the sponsors on what we can as well, attached are the logo for Hand in Hand Foundation, IV NFP, which is the nonprofit hosting the event, there is also a logo for Mosley Counsel, LLC which is one of the sponsors (this is so you have an idea of the other 4 or so that we would also want incorporated somehow). Please ask as many questions as you may have to clarify.

Industry/Entity Type

Event

Contact Information for Business Card

Hand in Hand
Nora T. Whitfield
President/CEO
(555)382-9046
www.handinhandfdn.example

New Card:
Peter J. Whitfield
Director
(555)309-6254
www.handinhandfdn.example

New Card:
Alice M. Whitfield
Director
www.handinhandfdn.example

New Card:
Gregory B. Whitfield
Director
www.handinhandfdn.example

Font styles to use
Script

Requirements
Must have
• I want a clean card for all 4 individuals with the logo that was attached.

```html
<!DOCTYPE html>
<html lang="en">
<head>
<meta charset="utf-8">
<title>Beer &amp; Wine Tasting with Appetizers</title>
<link rel="stylesheet" href="https://fonts.googleapis.com/css2?family=Abril+Fatface&family=Lobster&family=Open+Sans:wght@400;600&family=Cinzel&display=swap">
<style>
  :root {
    --ink: #0d0d0d;
    --wine: #6b1626;
    --wine-deep: #5a1020;
    --white: #ffffff;
    --amber: #e3a23a;
    --foam: #f3ead2;
    --dusk: #8b8a80;
  }
  html, body { margin: 0; padding: 0; overflow: hidden; }
  body { width: 848px; height: 1200px; }
  .flyer {
    position: relative;
    width: 848px;
    height: 1200px;
    overflow: hidden;
    background: var(--dusk);
  }
  .flyer__photo {
    position: absolute;
    inset: 0;
    background:
      radial-gradient(ellipse 360px 420px at 470px 520px, rgba(243,234,210,0.95), rgba(243,234,210,0) 70%),
      radial-gradient(ellipse 300px 260px at 520px 900px, rgba(214,120,30,0.9), rgba(214,120,30,0) 70%),
      radial-gradient(ellipse 520px 240px at 260px 230px, rgba(227,162,58,0.85), rgba(227,162,58,0) 70%),
      linear-gradient(180deg, #8e8a7c 0%, #c9a56a 25%, #d9c79c 50%, #b9ab8c 75%, #9a9686 100%);
  }
  .title {
    position: absolute;
    margin: 0;
    font-family: "Abril Fatface", serif;
    font-weight: 400;
    line-height: 1;
  }
  .title--beer { left: 8px; top: -38px; font-size: 212px; color: var(--ink); letter-spacing: -2px; }
  .title--amp { left: 417px; top: 134px; font-size: 44px; color: var(--wine); }
  .title--wine { left: 388px; top: 110px; font-size: 212px; color: var(--wine); letter-spacing: -2px; }
  .event-info {
    position: absolute;
    left: 583px; top: 20px;
    width: 265px; height: 130px;
    background: var(--ink);
    color: var(--white);
    font-family: "Open Sans", sans-serif;
    font-size: 15px;
    line-height: 28px;
    box-sizing: border-box;
    padding: 24px 18px 0 0;
    text-align: right;
  }
  .event-info p { margin: 0; }
  .tasting-band {
    position: absolute;
    left: 0; top: 540px;
    width: 848px; height: 192px;
    background: var(--ink);
    color: var(--white);
    text-align: center;
    font-family: "Lobster", cursive;
  }
  .tasting-band__line { margin: 0; text-transform: uppercase; }
  .tasting-band__line--top { font-size: 56px; padding-top: 18px; line-height: 64px; letter-spacing: 1px; }
  .tasting-band__line--main {
    font-size: 78px; line-height: 84px; letter-spacing: 2px;
    background: linear-gradient(180deg, var(--white) 55%, #cfcfcf 55%);
    -webkit-background-clip: text; background-clip: text; color: transparent;
  }
  .tag { position: absolute; top: 763px; width: 358px; height: 334px; color: var(--white); text-align: center; }
  .tag--tickets { left: 12px; }
  .tag--contact { left: 463px; }
  .tag__shape { position: absolute; inset: 0; }
  .tag__body { position: relative; }
  .tag__label { margin: 0; font-family: "Lobster", cursive; font-size: 36px; }
  .tag--tickets .tag__label { padding-top: 40px; }
  .tag--contact .tag__label { padding-top: 70px; font-size: 38px; }
  .tag__price { margin: 0; font-family: "Abril Fatface", serif; font-size: 104px; line-height: 110px; }
  .tag__phone { margin: 0; font-family: "Abril Fatface", serif; font-size: 40px; line-height: 46px; letter-spacing: 1px; }
  .tag__icon { display: block; margin: 0 auto; }
  .tag--tickets .tag__icon { margin-top: 14px; }
  .tag--contact .tag__icon { margin-top: 74px; }
  .sponsors { position: absolute; left: 0; top: 1078px; width: 848px; text-align: center; }
  .sponsors__heading { margin: 0; font-family: "Lobster", cursive; font-size: 27px; color: var(--ink); text-transform: uppercase; letter-spacing: 1px; }
  .sponsor { display: inline-flex; align-items: center; gap: 12px; margin-top: 10px; }
  .sponsor__mark { width: 34px; height: 34px; border-radius: 50%; border: 2px solid var(--ink); box-sizing: border-box; }
  .sponsor__name { font-family: "Cinzel", serif; font-size: 30px; color: var(--ink); }
</style>
</head>
<body>
<main class="flyer">
  <div class="flyer__photo" role="img" aria-label="Photograph of beer splashing from a glass mug with foam in warm amber light"></div>

  <h1 class="title title--beer">beer</h1>
  <span class="title title--amp">&amp;</span>
  <span class="title title--wine">wine</span>

  <section class="event-info">
    <p>May 9th from 6pm to 10pm</p>
    <p>Harborview Bistro</p>
    <p>Cedar Lake, Indiana, USA</p>
  </section>

  <section class="tasting-band">
    <p class="tasting-band__line tasting-band__line--top">Tasting with</p>
    <p class="tasting-band__line tasting-band__line--main">Appetizers</p>
  </section>

  <section class="tag tag--tickets">
    <svg class="tag__shape" viewBox="0 0 358 334" aria-hidden="true"><polygon points="0,0 358,0 358,258 179,334 0,258" fill="var(--wine)"/></svg>
    <div class="tag__body">
      <p class="tag__label">Tickets</p>
      <p class="tag__price">$100</p>
      <svg class="tag__icon" width="100" height="64" viewBox="0 0 100 64" aria-hidden="true">
        <g fill="var(--white)">
          <rect x="4" y="30" width="36" height="7" rx="3"/><rect x="4" y="39" width="36" height="7" rx="3"/>
          <rect x="4" y="48" width="36" height="7" rx="3"/><rect x="4" y="57" width="36" height="7" rx="3"/>
          <rect x="30" y="2" width="36" height="7" rx="3"/><rect x="30" y="11" width="36" height="7" rx="3"/>
          <rect x="30" y="20" width="36" height="7" rx="3"/><rect x="30" y="29" width="36" height="7" rx="3"/>
          <rect x="30" y="38" width="36" height="7" rx="3"/><rect x="30" y="47" width="36" height="7" rx="3"/>
          <circle cx="78" cy="46" r="18"/>
        </g>
        <text x="78" y="53" text-anchor="middle" font-family="Abril Fatface, serif" font-size="20" fill="var(--wine)">$</text>
      </svg>
    </div>
  </section>

  <section class="tag tag--contact">
    <svg class="tag__shape" viewBox="0 0 358 334" aria-hidden="true"><polygon points="0,0 358,0 358,258 179,334 0,258" fill="var(--wine)"/></svg>
    <div class="tag__body">
      <p class="tag__label">Contact us at</p>
      <p class="tag__phone">555-382-9046</p>
      <svg class="tag__icon" width="44" height="44" viewBox="0 0 24 24" aria-hidden="true">
        <path fill="var(--white)" d="M6.6 10.8a15.1 15.1 0 0 0 6.6 6.6l2.2-2.2c.3-.3.7-.4 1-.2 1.1.4 2.3.6 3.6.6.6 0 1 .4 1 1V20c0 .6-.4 1-1 1A17 17 0 0 1 3 4c0-.6.4-1 1-1h3.5c.6 0 1 .4 1 1 0 1.3.2 2.5.6 3.6.1.3 0 .7-.2 1z"/>
      </svg>
    </div>
  </section>

  <footer class="sponsors">
    <p class="sponsors__heading">Sponsors include</p>
    <div class="sponsor">
      <span class="sponsor__mark" aria-hidden="true"></span>
      <span class="sponsor__name">Mosley Counsel, LLC</span>
    </div>
  </footer>
</main>
</body>
</html>
```